Design a presentation folder for medical imaging company

I am looking for a presentation folder (for holding 8.5 x 11 paper) )design in adobe illustrator that can easily be printed by online companies like [login to view URL], [login to view URL], folvanprintery.com.

Logo design and stationary design already in use are attached. Color scheme is open but logo should be incorporated. Do not know if it would work well but would like to see one with primarily black as well as other white/blue (logo colors) but am open to other colors that fit the professional look of a medical imaging company, dealing with xrays, ultrasounds, CT's, MRI, etc.

All of the items attached do not need to be used in the design, but to give an idea of some of current marketing materials. The winning design will get final logo files, higher resolution graphics if needed, from attached files, and contact info to complete project.

Final deliverable should be adobe illustrator files, for standard size presntation folders, pockets, no pockets, w/wo business card slot

```html
<!DOCTYPE html>
<html lang="en">
<head>
<meta charset="utf-8">
<title>Veridan Radiology – Presentation Folder Dieline</title>
<link rel="stylesheet" href="https://fonts.googleapis.com/css2?family=Open+Sans:wght@400;600&display=swap">
<style>
  :root {
    --paper: #ffffff;
    --folder-grey: #9b9a9b;
    --folder-edge: #7c7b7c;
    --band-navy: #263f6e;
    --type-white: #ffffff;
    --crop-mark: #9a9a9a;
    --mark-disc: #dfe5ee;
  }
  html, body {
    margin: 0;
    padding: 0;
    width: 1200px;
    height: 1105px;
    overflow: hidden;
    background: var(--paper);
  }
  .folder-sheet {
    display: block;
    width: 1200px;
    height: 1105px;
    font-family: "Open Sans", Arial, sans-serif;
  }
  .folder-body, .pocket-flap {
    fill: var(--folder-grey);
    stroke: var(--folder-edge);
    stroke-width: 1.5;
  }
  .brand-band { fill: var(--band-navy); }
  .crop-marks line { stroke: var(--crop-mark); stroke-width: 0.8; }
  .band-divider { stroke: var(--type-white); stroke-width: 1; }
  .contact-label, .contact-line {
    fill: var(--type-white);
    font-size: 6.5px;
    font-weight: 400;
  }
  .brand-disc { fill: var(--mark-disc); stroke: var(--type-white); stroke-width: 1.5; }
  .brand-name {
    fill: var(--type-white);
    font-size: 9.5px;
    font-weight: 400;
    letter-spacing: 0.3px;
  }
  .brand-name-strong {
    fill: var(--type-white);
    font-size: 11px;
    font-weight: 400;
    letter-spacing: 2px;
  }
  .site-address {
    fill: var(--type-white);
    font-size: 9.5px;
    font-weight: 400;
  }
  .contact-icon { fill: var(--type-white); }
</style>
</head>
<body>
<svg class="folder-sheet" viewBox="0 0 1200 1105" xmlns="http://www.w3.org/2000/svg">
  <defs>
    <radialGradient id="tone-anatomy" cx="0.68" cy="0.55" r="0.75">
      <stop offset="0" stop-color="#4aa8ff"/>
      <stop offset="0.4" stop-color="#1f5fb8"/>
      <stop offset="1" stop-color="#0a1630"/>
    </radialGradient>
    <radialGradient id="tone-ultrasound" cx="0.5" cy="0.6" r="0.55">
      <stop offset="0" stop-color="#6a6a6a"/>
      <stop offset="0.5" stop-color="#262626"/>
      <stop offset="1" stop-color="#030303"/>
    </radialGradient>
    <linearGradient id="tone-scans" x1="0" y1="0" x2="0" y2="1">
      <stop offset="0" stop-color="#efe7d8"/>
      <stop offset="0.35" stop-color="#b8b2a3"/>
      <stop offset="0.55" stop-color="#3f7180"/>
      <stop offset="1" stop-color="#0e2229"/>
    </linearGradient>
    <radialGradient id="tone-scanner" cx="0.08" cy="0.55" r="0.9">
      <stop offset="0" stop-color="#cfe0ff"/>
      <stop offset="0.2" stop-color="#4b74e0"/>
      <stop offset="0.6" stop-color="#1b2f86"/>
      <stop offset="1" stop-color="#070c26"/>
    </radialGradient>
  </defs>

  <!-- trim marks -->
  <g class="crop-marks">
    <line x1="80" y1="14" x2="80" y2="40"/>
    <line x1="600" y1="14" x2="600" y2="40"/>
    <line x1="1115" y1="14" x2="1115" y2="40"/>
    <line x1="40" y1="59" x2="66" y2="59"/>
    <line x1="1131" y1="59" x2="1160" y2="59"/>
    <line x1="40" y1="835" x2="62" y2="835"/>
    <line x1="1131" y1="835" x2="1160" y2="835"/>
    <line x1="600" y1="853" x2="600" y2="880"/>
    <line x1="1115" y1="853" x2="1115" y2="880"/>
    <line x1="80" y1="1088" x2="80" y2="1105"/>
  </g>

  <!-- folder surfaces -->
  <path class="pocket-flap" d="M72 836 L46 844 L46 1078 Q46 1087 55 1087 L228 1087 C400 1087 544 985 544 870 L544 836 Z"/>
  <rect class="folder-body" x="72" y="51" width="1051" height="785"/>

  <!-- cover imagery column -->
  <g class="imagery-column">
    <rect x="600" y="51" width="197" height="142" fill="url(#tone-anatomy)" role="img" aria-label="Photo: glowing blue anatomical figure study"/>
    <rect x="600" y="197" width="197" height="135" fill="url(#tone-ultrasound)" role="img" aria-label="Photo: ultrasound scan image"/>
    <rect x="600" y="336" width="197" height="137" fill="url(#tone-scans)" role="img" aria-label="Photo: monitors displaying MRI brain scans"/>
    <rect x="600" y="477" width="197" height="131" fill="url(#tone-scanner)" role="img" aria-label="Photo: CT scanner room lit in blue"/>
  </g>

  <!-- brand band -->
  <rect class="brand-band" x="72" y="608" width="1051" height="95"/>

  <g class="back-contact">
    <text class="contact-label" x="174" y="645">company</text>
    <text class="contact-label" x="174" y="656">address</text>
    <text class="contact-label" x="174" y="667">state</text>
    <line class="band-divider" x1="216" y1="622" x2="216" y2="690"/>
    <path class="contact-icon" d="M225 638 q0 -2 2 -2 l1.5 2 -1.5 1.5 q1 2 3 3 l1.5 -1.5 2 1.5 q0 2 -2 2 q-6.5 -0.5 -6.5 -6.5z"/>
    <text class="contact-line" x="240" y="644">1-555-555-1212</text>
    <rect class="contact-icon" x="225" y="652" width="7" height="5"/>
    <rect class="contact-icon" x="226.5" y="650" width="4" height="2"/>
    <text class="contact-line" x="240" y="656">1-555-555-1212</text>
    <rect class="contact-icon" x="225" y="663" width="7" height="5"/>
    <text class="contact-line" x="240" y="668">info@email.com</text>
    <text class="contact-line" x="240" y="680">www.url.com</text>
    <line class="band-divider" x1="323" y1="622" x2="323" y2="690"/>
  </g>

  <g class="brand-lockup back-lockup">
    <circle class="brand-disc" cx="370" cy="656" r="22"/>
    <text class="brand-name" x="407" y="653">VERIDAN IMAGING GROUP</text>
    <text class="brand-name-strong" x="470" y="669" text-anchor="middle">RADIOLOGY</text>
  </g>

  <g class="brand-lockup front-lockup">
    <circle class="brand-disc" cx="890" cy="656" r="22"/>
    <text class="brand-name" x="927" y="653">VERIDAN IMAGING GROUP</text>
    <text class="brand-name-strong" x="990" y="669" text-anchor="middle">RADIOLOGY</text>
  </g>

  <text class="site-address" x="1025" y="816">www.url.com</text>

  <!-- pocket lockup, printed upside down so it reads when folded -->
  <g class="brand-lockup pocket-lockup" transform="rotate(180 300 935)">
    <circle class="brand-disc" cx="250" cy="935" r="21"/>
    <text class="brand-name" x="286" y="932">VERIDAN IMAGING GROUP</text>
    <text class="brand-name-strong" x="349" y="948" text-anchor="middle">RADIOLOGY</text>
  </g>
</svg>
</body>
</html>
```